Business card for Real Estate Company located in Coastal area of spain

Want a business card design. Simple, professional, horizontal layout. will be 2 sided. Name of company (logo big on front). Name of agent, phone and email address. Back side will be list of general services we provide. Would like to see 2 separate concepts using the 2 separate logo treatments. One using Rich dark, bright blue as the stock color, and the other using White as the stock color.
Logo files uploaded (2 different versions) Domain (bayridgedwell48.com) Moraira-Calpe-Altea-Javea-Denia-Marina Alta Area (perhaps across the bottom of the front of card0 Petra Linde Licensed Estate Agent / Partner Petra@bayridgedwell48.com +34.681.72.40.96 Back of card should list services offered

Real Estate Sales and Investments Real Estate Rental Management Kitchen, Bathroom Reformations Complete Home Reformation Services Window and Door Replacement Landscape and Garden Management Pool and Jacuzzi Service

Target Market(s)

Real estate and construction

Industry/Entity Type

Real Estate

Contact Information for Business Card

Logo files uploaded (2 different versions) Domain (bayridgedwell48.com) Moraira-Calpe-Altea-Javea-Denia-Marina Alta Area (perhaps across the bottom of the front of card0 Petra Linde Licensed Estate Agent / Partner Petra@bayridgedwell48.com +34.681.72.40.96

Colors

Designer to choose colors to be used in the design.

Requirements
Must have
• progressive look professional
Nice to have
• Front big logo, Agent details. Back, list of services included in project description
Should not have
• Gloss finish for card

```html
<!DOCTYPE html>
<html lang="en">
<head>
<meta charset="utf-8">
<title>Bayridgedwell48.com – Business Card</title>
<link rel="stylesheet" href="https://fonts.googleapis.com/css2?family=Questrial&family=Montserrat:wght@400;500;700&display=swap">
<style>
  :root {
    --backdrop: #bfbfc0;
    --label: #5a5a5a;
    --navy: #040c2e;
    --blue: #4b5fb1;
    --violet: #8a66b4;
    --pink: #b266a8;
    --name: #e6e6ee;
    --paper: #ffffff;
    --ink: #111111;
    --lilac-top: #e2d2e8;
    --lilac-bottom: #c9c6e6;
  }
  * { box-sizing: border-box; margin: 0; padding: 0; }
  html, body {
    width: 877px; height: 1200px; overflow: hidden;
    background: var(--backdrop);
    font-family: "Montserrat", sans-serif;
  }
  .side-label {
    position: absolute; right: 56px;
    font: 700 26px "Montserrat", sans-serif;
    color: var(--label);
  }
  .side-label.front-label { top: 14px; }
  .side-label.back-label { top: 1142px; }

  .card {
    position: absolute; left: 42px; width: 777px; height: 520px;
    box-shadow: 6px 10px 14px rgba(0,0,0,0.35);
    overflow: hidden;
  }
  .card-front { top: 54px; background: var(--navy); text-align: center; }
  .card-back { top: 614px; background: var(--paper); }

  .brand-name {
    font-family: "Questrial", sans-serif; font-weight: 400;
    color: var(--violet); white-space: nowrap;
  }
  .card-front .brand-name {
    position: absolute; left: 0; right: 0; top: 64px;
    font-size: 60px; line-height: 1;
  }
  .tagline {
    font-weight: 700; letter-spacing: 0.32em; white-space: nowrap;
    text-transform: uppercase;
  }
  .card-front .tagline {
    position: absolute; left: 0; right: 0; top: 136px;
    font-size: 14px; color: var(--violet);
  }
  .agent-rule {
    position: absolute; top: 220px; height: 2px;
    background: linear-gradient(90deg, var(--blue), var(--pink));
  }
  .agent-rule.left { left: 68px; width: 208px; }
  .agent-rule.right { left: 499px; width: 210px; background: linear-gradient(90deg, var(--pink), var(--blue)); }
  .agent-name {
    position: absolute; left: 0; right: 0; top: 204px;
    font-size: 26px; font-weight: 500; color: var(--name);
  }
  .agent-title {
    position: absolute; left: 0; right: 0; top: 243px;
    font-size: 16px; color: var(--blue);
  }
  .contact { position: absolute; left: 0; right: 0; color: var(--blue); }
  .contact.phone { top: 325px; font-size: 25px; }
  .contact.email { top: 373px; font-size: 20px; }
  .contact.area { top: 419px; font-size: 20px; }

  .skyline-art {
    position: absolute; left: 0; top: 123px; width: 263px; height: 397px;
    background: linear-gradient(180deg, var(--lilac-top), var(--lilac-bottom));
  }
  .brand-band { position: absolute; left: 263px; top: 61px; width: 514px; height: 70px; }
  .card-back .brand-name {
    position: absolute; left: 43px; top: 11px;
    font-size: 37px; line-height: 1; color: var(--paper);
  }
  .card-back .tagline {
    position: absolute; left: 62px; top: 52px;
    font-size: 9.5px; letter-spacing: 0.3em; color: var(--paper);
  }
  .service-list {
    position: absolute; left: 301px; top: 169px; list-style: none;
  }
  .service-list li {
    position: relative; padding-left: 21px;
    font-size: 17px; font-weight: 500; color: var(--ink);
    height: 38.8px; line-height: 24px; white-space: nowrap;
  }
  .service-list li::before {
    content: ""; position: absolute; left: 0; top: 7px;
    width: 11px; height: 11px; border-radius: 50%; background: var(--ink);
  }
</style>
</head>
<body>
  <div class="side-label front-label">Front</div>

  <section class="card card-front">
    <div class="brand-name">Bayridgedwell48.com</div>
    <div class="tagline">Real Estate-Reforms-Home Services</div>
    <div class="agent-rule left"></div>
    <div class="agent-name">Petra Linde</div>
    <div class="agent-rule right"></div>
    <div class="agent-title">Licensed Estate Agent / Partner</div>
    <div class="contact phone">+34.681.72.40.96</div>
    <div class="contact email">Petra@bayridgedwell48.com</div>
    <div class="contact area">Moraira-Calpe-Altea-Javea-Denia-Marina Alta Area</div>
  </section>

  <section class="card card-back">
    <div class="skyline-art" role="img" aria-label="Illustration of a city skyline with tall gradient buildings"></div>
    <div class="brand-band">
      <svg width="514" height="70" viewBox="0 0 514 70" aria-hidden="true">
        <defs>
          <linearGradient id="bandFill" x1="0" y1="1" x2="1" y2="0">
            <stop offset="0" stop-color="#4b5fb1"/>
            <stop offset="0.45" stop-color="#8a66b4"/>
            <stop offset="1" stop-color="#b266a8"/>
          </linearGradient>
        </defs>
        <polygon points="0,0 514,0 514,70 26,70" fill="url(#bandFill)"/>
      </svg>
      <div class="brand-name">Bayridgedwell48.com</div>
      <div class="tagline">Real Estate-Reforms-Home Services</div>
    </div>
    <ul class="service-list">
      <li>Real Estate Sales and Investments</li>
      <li>Real Estate Rental Management</li>
      <li>Kitchen, Bathroom Reformations</li>
      <li>Complete Home Reformation Services</li>
      <li>Window and Door Replacement</li>
      <li>Landscape and Garden Management</li>
      <li>Pool and Jacuzzi Service</li>
    </ul>
  </section>

  <div class="side-label back-label">Back</div>
</body>
</html>
```